Business Card for a Floral & Decorating Business

I would like to take my current logo and create a better business card. I am looking for elegance as I am a florist and event decorator. My logo has multiple colour options. I like colours like green, purple, pink and orange, I think I would like a white card, open to black back ground. I want it to feel elegant and romantic. I like metallic lettering that maybe is indented in the paper, I also like glossy paper. I have a full logo already as well as a badge. I have attached both in multiple colours.m
Updates

Need extra days to review

Target Market(s)

Weddings, special events, floral customers

Industry/Entity Type

Floral and decorating

Contact Information for Business Card

Phone number, email, instagram, facebook, title, name, logo

Font styles to use
Script

Requirements
Nice to have
• Elegant

```html
<!DOCTYPE html>
<html lang="en">
<head>
<meta charset="utf-8">
<title>Wrenfield Hale – Business Card</title>
<link href="https://fonts.googleapis.com/css2?family=Montserrat:wght@400;700&family=Allura&display=swap" rel="stylesheet">
<style>
  :root {
    --backdrop: #e4e4e3;
    --teal: #628b82;
    --teal-deep: #517a70;
    --teal-soft: #9dbdb5;
    --ink-light: #ffffff;
    --paper: #fbfbfa;
    --edge: #3f3f3f;
  }
  * { margin: 0; padding: 0; box-sizing: border-box; }
  html, body { width: 1200px; height: 1200px; overflow: hidden; }
  body {
    background: var(--backdrop);
    font-family: "Montserrat", sans-serif;
    position: relative;
  }
  .card {
    position: absolute;
    left: 262px;
    width: 686px;
    height: 392px;
    border-radius: 19px;
    overflow: hidden;
  }
  .card--front { top: 165px; }
  .card--back {
    top: 653px;
    background: linear-gradient(180deg, var(--teal) 0%, var(--teal-deep) 100%);
  }
  .card-bg { position: absolute; inset: 0; }

  .brand {
    position: absolute;
    text-align: center;
    color: var(--teal);
  }
  .brand-name {
    font-weight: 400;
    font-size: 26px;
    letter-spacing: 1px;
  }
  .brand-tagline {
    font-weight: 400;
    font-size: 9px;
    letter-spacing: 2.6px;
    margin-top: 8px;
  }
  .card--front .brand { left: 22px; width: 300px; top: 168px; }
  .card--back .brand { left: 0; width: 686px; top: 195px; color: var(--teal-soft); }
  .card--back .brand-name { font-size: 34px; }
  .card--back .brand-tagline { font-size: 11px; letter-spacing: 3.4px; margin-top: 12px; }

  .details {
    position: absolute;
    left: 392px;
    top: 104px;
    color: var(--ink-light);
  }
  .person-name { font-weight: 700; font-size: 21px; line-height: 1; }
  .person-title {
    font-family: "Allura", cursive;
    font-size: 27px;
    line-height: 1;
    margin-top: 2px;
    margin-left: 4px;
  }
  .address {
    font-size: 15px;
    line-height: 19px;
    margin-top: 22px;
    margin-left: 8px;
  }
  .contact-list { list-style: none; margin-top: 14px; margin-left: 8px; }
  .contact-list li {
    display: flex;
    align-items: center;
    font-size: 15px;
    line-height: 20px;
  }
  .contact-list svg { width: 14px; height: 14px; margin-right: 12px; fill: var(--ink-light); }

  .social {
    position: absolute;
    top: 320px;
    left: 0;
    width: 686px;
    display: flex;
    justify-content: center;
    gap: 4px;
  }
  .social-dot {
    width: 29px;
    height: 29px;
    border-radius: 50%;
    background: var(--teal-soft);
    opacity: 0.55;
  }
</style>
</head>
<body>

<section class="card card--front" aria-label="Card front">
  <svg class="card-bg" viewBox="0 0 686 392" preserveAspectRatio="none" aria-hidden="true">
    <defs>
      <linearGradient id="tealFill" x1="0" y1="0" x2="0" y2="1">
        <stop offset="0" stop-color="#658e85"/>
        <stop offset="1" stop-color="#517a70"/>
      </linearGradient>
    </defs>
    <rect width="686" height="392" fill="url(#tealFill)"/>
    <path d="M0 0 H328 Q380 190 318 392 H0 Z" fill="#3f3f3f"/>
    <path d="M0 0 H320 Q372 190 306 392 H0 Z" fill="#fbfbfa"/>
  </svg>

  <div class="brand">
    <div class="brand-name">Wrenfield Hale</div>
    <div class="brand-tagline">DECORATING &amp; FLORALS.</div>
  </div>

  <div class="details">
    <div class="person-name">Martin Ellory</div>
    <div class="person-title">Florist</div>
    <div class="address">214 Larkspur Road<br>Juneau, Alaska 99801</div>
    <ul class="contact-list">
      <li>
        <svg viewBox="0 0 24 24" aria-hidden="true"><path d="M6.6 10.8a15.1 15.1 0 0 0 6.6 6.6l2.2-2.2c.3-.3.7-.4 1-.2 1.1.4 2.3.6 3.6.6.6 0 1 .4 1 1V20c0 .6-.4 1-1 1A17 17 0 0 1 3 4c0-.6.4-1 1-1h3.5c.6 0 1 .4 1 1 0 1.3.2 2.5.6 3.6.1.3 0 .7-.2 1z"/></svg>
        555-201-4470
      </li>
      <li>
        <svg viewBox="0 0 24 24" aria-hidden="true"><path d="M2 5h20v14H2z M4 7v.5l8 5 8-5V7l-8 5z" fill-rule="evenodd"/></svg>
        hello@wrenfieldhale.com
      </li>
      <li>
        <svg viewBox="0 0 24 24" aria-hidden="true"><circle cx="12" cy="12" r="10"/></svg>
        www.wrenfieldhale.com
      </li>
    </ul>
  </div>
</section>

<section class="card card--back" aria-label="Card back">
  <div class="brand">
    <div class="brand-name">Wrenfield Hale</div>
    <div class="brand-tagline">DECORATING &amp; FLORALS.</div>
  </div>
  <div class="social" aria-label="Social media links">
    <span class="social-dot"></span>
    <span class="social-dot"></span>
  </div>
</section>

</body>
</html>
```